Real Estate Company
Residential & Commercial
Sales & Property Management

would like to use the logo i uploaded but would really love a black back ground...I think with the gold fleur dis lis and the maroon lettering it would really look great!

Industry/Entity Type

Business

Contact Information for Business Card

Bright Harbor Real Estate Co.
Danielle Forsythe
Broker/Owner
555-204-7731 Cell
555-862-4190 Office
4812 Pellan Rd Alderton OR 97599

```html
<!DOCTYPE html>
<html lang="en">
<head>
<meta charset="utf-8">
<title>Bright Harbor Real Estate Co. – Business Card</title>
<link href="https://fonts.googleapis.com/css2?family=Roboto+Condensed:wght@400;700&display=swap" rel="stylesheet">
<style>
  :root {
    --page: #ffffff;
    --charcoal: #2b2b2c;
    --charcoal-light: #454546;
    --brand-red: #c4252f;
    --cream: #f1dca0;
    --logo-cream: #fbf0c4;
    --ink: #231f20;
  }
  * { margin: 0; padding: 0; box-sizing: border-box; }
  html, body {
    width: 1200px;
    height: 960px;
    overflow: hidden;
    background: var(--page);
    font-family: "Roboto Condensed", "Arial Narrow", sans-serif;
  }
  .business-card {
    position: absolute;
    left: 180px;
    top: 238px;
    width: 840px;
    height: 484px;
    overflow: hidden;
    background: var(--cream);
  }
  .card-art {
    position: absolute;
    inset: 0;
    width: 840px;
    height: 484px;
  }
  .company-name {
    position: absolute;
    left: 56px;
    top: 100px;
    color: var(--logo-cream);
    font-weight: 700;
    font-size: 58px;
    line-height: 1.05;
    letter-spacing: -0.8px;
  }
  .contact-block {
    position: absolute;
    right: 38px;
    top: 344px;
    text-align: right;
    color: var(--ink);
    font-size: 30px;
    line-height: 38.5px;
    font-weight: 400;
    letter-spacing: -0.45px;
    white-space: nowrap;
  }
  .contact-name { font-weight: 700; }
</style>
</head>
<body>
  <div class="business-card">
    <svg class="card-art" viewBox="0 0 840 484" xmlns="http://www.w3.org/2000/svg">
      <defs>
        <linearGradient id="houseTone" x1="0" y1="0" x2="1" y2="1">
          <stop offset="0" stop-color="var(--charcoal-light)"/>
          <stop offset="0.5" stop-color="var(--charcoal)"/>
          <stop offset="1" stop-color="var(--charcoal-light)"/>
        </linearGradient>
        <linearGradient id="bandShadow" x1="0" y1="0" x2="0" y2="1">
          <stop offset="0" stop-color="#000" stop-opacity="0.35"/>
          <stop offset="1" stop-color="#000" stop-opacity="0"/>
        </linearGradient>
      </defs>
      <path class="house-photo" role="img" aria-label="Blurred photo of a large two-story house in dark tones"
            d="M0 0 H840 V216 Q560 300 0 309 Z" fill="url(#houseTone)"/>
      <path class="band-shadow" d="M0 353 Q520 345 840 242 V256 Q520 362 0 368 Z" fill="url(#bandShadow)"/>
      <path class="red-swoosh" d="M0 309 Q560 300 840 216 V242 Q520 345 0 353 Z" fill="var(--brand-red)"/>
    </svg>

    <div class="company-name">Bright Harbor<br>Real Estate Co.</div>

    <div class="contact-block">
      <div><span class="contact-name">Danielle Forsythe,</span> Broker/Owner</div>
      <div>555.204.7731 Cell • 555.862.4190 Office</div>
      <div>4812 Pellan Rd., Alderton OR 97599</div>
    </div>
  </div>
</body>
</html>
```